New Crowdfunding site Fundlark needs banner ads

I’m looking for 4 standard size banner ads for www.fundlark.example to be used by TradeQuill Affiliates in order to bring new crowdfunding projects to the platform.
728x90
160x600
300x250
180x160

Succesful designers will put on our Mentors list so that the project owner can also get their specific project banners from our designers. Designers can also become our affiliates either to promote Fundlark.example or individual projects.
Updates

Please note updated brief

Thank you to those that have submitted designs so far.
Please be reminded that the invitation will close tomorrow after which we will make our choice

Thanks for input so far.
Please note project closes tomorrow (Sunday) after which we will choose.

Target Market(s)

Target is a project owner with a project requiring $10,000 or more in any field including business and/or non-profits. Any country.
Inventors, creatives, communities, hardware or software, consumer items,

Industry/Entity Type

Crowdfunding

Font styles to use
Sans Serif

Requirements
Must have
• Clear button call to action based on our USPs shown on the home page but especially the use of Affiliate Networks to promote their project to the widest possible audience.

Text and button text should be editable (see png preference).
Call to action could be based on "Free Crowdfunding Consultation - is your project viable" or "Get Your Free Guide to Succesful Crowdfunding"
Nice to have
• .png format preferred with separate objects.
Some animation preferred in the button.

```html
<!DOCTYPE html>
<html lang="en">
<head>
<meta charset="utf-8">
<title>Fundlark banner set</title>
<link rel="stylesheet" href="https://fonts.googleapis.com/css2?family=Open+Sans:wght@400;600&display=swap">
<style>
  :root{
    --ink-blue:#1f4f72;
    --brand-blue:#1212d8;
    --text-dark:#222;
    --white:#fff;
    --green-top:#9be85a;
    --green-bottom:#4cb51c;
    --green-text:#7fe040;
    --pink:#ff3ef0;
    --navy:#161a57;
    --violet:#5b2b8e;
    --sky:#3f86d6;
    --deep-sky:#1f4d94;
    --plum:#7a1b6e;
    --orchid:#b04aa6;
    --charcoal:#2e2e2e;
    --slate:#6a6a6a;
    --logo-dot:#6a3fd6;
  }
  *{margin:0;padding:0;box-sizing:border-box}
  html,body{width:1200px;height:900px;overflow:hidden;background:var(--white)}
  body{position:relative;font-family:"Open Sans",Arial,sans-serif;color:var(--white)}
  .abs{position:absolute}
  .line{position:absolute;white-space:nowrap;line-height:1}
  .shadow{text-shadow:2px 3px 4px rgba(0,0,0,.55)}

  /* brand lockups */
  .brand-dot{position:absolute;border-radius:50%;background:var(--logo-dot)}
  .brand-name{color:var(--ink-blue);font-weight:400}
  .brand-tag{color:var(--text-dark)}
  .brand-name.vertical{color:var(--brand-blue)}

  /* backgrounds */
  .bg-night{background:linear-gradient(120deg,var(--navy) 0%,#23307a 45%,var(--violet) 85%,#8a3aa0 100%)}
  .bg-sky{background:linear-gradient(180deg,var(--sky) 0%,#4d8fd9 55%,#8fb4df 68%,var(--deep-sky) 100%)}
  .bg-plum{background:linear-gradient(160deg,#9a4a94 0%,var(--plum) 35%,#5e1359 65%,var(--orchid) 100%)}
  .bg-charcoal{background:linear-gradient(165deg,#1f1f1f 0%,var(--charcoal) 40%,var(--slate) 80%,#8a8a8a 100%)}
  .bg-deep{background:linear-gradient(170deg,#0e1240 0%,#1c2370 40%,#2f3fb0 80%,#3b5ad0 100%)}

  .zig-left{clip-path:polygon(0 0,100% 0,100% 100%,0 100%,7px 94.4%,0 88.9%,7px 83.3%,0 77.8%,7px 72.2%,0 66.7%,7px 61.1%,0 55.6%,7px 50%,0 44.4%,7px 38.9%,0 33.3%,7px 27.8%,0 22.2%,7px 16.7%,0 11.1%,7px 5.6%)}
  .zig-top{clip-path:polygon(0 0,5% 8px,10% 0,15% 8px,20% 0,25% 8px,30% 0,35% 8px,40% 0,45% 8px,50% 0,55% 8px,60% 0,65% 8px,70% 0,75% 8px,80% 0,85% 8px,90% 0,95% 8px,100% 0,100% 100%,0 100%)}

  .banner{position:absolute;overflow:hidden}
  .foot-strip{position:absolute;left:0;right:0;bottom:0;height:16px;background:#000}

  /* call-to-action button */
  .cta{position:absolute;display:flex;align-items:center;justify-content:space-between;
       padding:0 8px 0 12px;border-radius:6px;color:#1b2b10;font-size:14px;
       background:linear-gradient(180deg,var(--green-top),var(--green-bottom));
       box-shadow:2px 3px 5px rgba(0,0,0,.45)}
  .cta svg{width:18px;height:18px;flex:none}
  .cta.tall{font-size:14px}
</style>
</head>
<body>

<!-- leaderboard: consultation -->
<div class="brand-dot" style="left:18px;top:58px;width:46px;height:46px"></div>
<div class="line brand-name" style="left:70px;top:60px;font-size:25px">Fundlark</div>
<div class="line brand-tag" style="left:71px;top:91px;font-size:12px">Project +&nbsp; Crowdfunding</div>
<div class="banner bg-night zig-left" style="left:215px;top:35px;width:530px;height:90px" role="img" aria-label="Dark blue and violet faceted background">
  <div class="line" style="left:25px;top:27px;font-size:18px">FREE CROWDFUNDING CONSULTATION</div>
  <div class="line" style="left:226px;top:56px;font-size:13px">IS YOUR PROJECT VIABLE</div>
  <div class="cta" style="left:404px;top:40px;width:117px;height:33px"><span>Learn More</span>
    <svg viewBox="0 0 18 18"><circle cx="9" cy="9" r="8" fill="#fff"/><path d="M7 5l5 4-5 4z" fill="#4cb51c"/></svg></div>
</div>

<!-- leaderboard: guide -->
<div class="brand-dot" style="left:18px;top:166px;width:46px;height:46px"></div>
<div class="line brand-name" style="left:70px;top:168px;font-size:25px">Fundlark</div>
<div class="line brand-tag" style="left:71px;top:199px;font-size:12px">Project +&nbsp; Crowdfunding</div>
<div class="banner bg-sky zig-left" style="left:215px;top:143px;width:530px;height:90px" role="img" aria-label="Bright blue faceted background">
  <div class="line" style="left:32px;top:23px;font-size:17px">GET YOUR FREE GUIDE TO</div>
  <div class="line" style="left:51px;top:45px;font-size:22px">SUCCESSFUL CROWDFUNDING</div>
  <div class="cta" style="left:404px;top:40px;width:117px;height:34px"><span>Learn More</span>
    <svg viewBox="0 0 18 18"><circle cx="9" cy="9" r="8" fill="#fff"/><path d="M7 5l5 4-5 4z" fill="#4cb51c"/></svg></div>
</div>

<!-- medium rectangle: blue -->
<div class="banner bg-sky" style="left:851px;top:35px;width:300px;height:250px" role="img" aria-label="Blue faceted background">
  <svg class="abs" style="left:0;top:0" width="300" height="120" viewBox="0 0 300 120"><path d="M0 0H300V15Q150 118 0 28Z" fill="#fff"/></svg>
  <div class="brand-dot" style="left:26px;top:6px;width:38px;height:38px"></div>
  <div class="line brand-name" style="left:83px;top:7px;font-size:23px">Fundlark</div>
  <div class="line brand-tag" style="left:73px;top:36px;font-size:13px">Project + Crowd = FUNDING</div>
  <div class="line shadow" style="left:0;right:0;text-align:center;top:86px;font-size:23px">FREE</div>
  <div class="line shadow" style="left:0;right:0;text-align:center;top:117px;font-size:25px">CROWDFUNDING</div>
  <div class="line shadow" style="left:0;right:0;text-align:center;top:143px;font-size:25px">CONSULTATION</div>
  <div class="line" style="left:0;right:0;text-align:center;top:182px;font-size:14px">IS YOUR PROJECT VIABLE</div>
  <div class="cta" style="left:94px;top:210px;width:118px;height:33px"><span>Learn More</span>
    <svg viewBox="0 0 18 18"><circle cx="9" cy="9" r="8" fill="#fff"/><path d="M7 5l5 4-5 4z" fill="#4cb51c"/></svg></div>
</div>

<!-- medium rectangle: night -->
<div class="banner bg-night" style="left:851px;top:317px;width:300px;height:250px" role="img" aria-label="Dark blue and violet faceted background">
  <svg class="abs" style="left:0;top:0" width="300" height="120" viewBox="0 0 300 120"><path d="M0 0H300V15Q150 118 0 28Z" fill="#fff"/></svg>
  <div class="brand-dot" style="left:26px;top:6px;width:38px;height:38px"></div>
  <div class="line brand-name" style="left:83px;top:7px;font-size:23px">Fundlark</div>
  <div class="line brand-tag" style="left:73px;top:36px;font-size:13px">Project + Crowd = FUNDING</div>
  <div class="line shadow" style="left:0;right:0;text-align:center;top:86px;font-size:23px">FREE</div>
  <div class="line shadow" style="left:0;right:0;text-align:center;top:117px;font-size:25px">CROWDFUNDING</div>
  <div class="line shadow" style="left:0;right:0;text-align:center;top:143px;font-size:25px">CONSULTATION</div>
  <div class="line" style="left:0;right:0;text-align:center;top:182px;font-size:14px">IS YOUR PROJECT VIABLE</div>
  <div class="cta" style="left:94px;top:210px;width:118px;height:33px"><span>Learn More</span>
    <svg viewBox="0 0 18 18"><circle cx="9" cy="9" r="8" fill="#fff"/><path d="M7 5l5 4-5 4z" fill="#4cb51c"/></svg></div>
</div>

<!-- skyscraper: plum -->
<div class="brand-dot" style="left:75px;top:295px;width:66px;height:66px"></div>
<div class="line brand-name vertical" style="left:27px;width:160px;text-align:center;top:362px;font-size:22px">Fundlark</div>
<div class="line brand-tag" style="left:27px;width:160px;text-align:center;top:389px;font-size:13px;line-height:14.5px;white-space:normal">Project + Crowd<br>=<br>Funding</div>
<div class="banner bg-plum zig-top" style="left:27px;top:443px;width:160px;height:445px" role="img" aria-label="Purple faceted background">
  <div class="line shadow" style="left:0;right:0;text-align:center;top:78px;font-size:21px">GET YOUR</div>
  <div class="line shadow" style="left:12px;top:144px;font-size:32px;color:var(--green-text)">FREE</div>
  <div class="line shadow" style="right:12px;top:182px;font-size:30px;color:var(--green-text)">GUIDE</div>
  <div class="line shadow" style="left:0;right:0;text-align:center;top:264px;font-size:23px">SUCCESSFUL</div>
  <div class="line shadow" style="left:0;right:0;text-align:center;top:291px;font-size:17px">CROWDFUNDING</div>
  <div class="cta tall" style="left:9px;top:393px;width:143px;height:38px"><span>LEARN MORE</span>
    <svg viewBox="0 0 18 18"><circle cx="9" cy="9" r="8" fill="#fff"/><path d="M7 5l5 4-5 4z" fill="#4cb51c"/></svg></div>
  <div class="foot-strip"></div>
</div>

<!-- skyscraper: charcoal -->
<div class="brand-dot" style="left:257px;top:295px;width:66px;height:66px"></div>
<div class="line brand-name vertical" style="left:209px;width:160px;text-align:center;top:362px;font-size:22px">Fundlark</div>
<div class="line brand-tag" style="left:209px;width:160px;text-align:center;top:389px;font-size:13px;line-height:14.5px;white-space:normal">Project + Crowd<br>=<br>Funding</div>
<div class="banner bg-charcoal zig-top" style="left:209px;top:443px;width:160px;height:445px" role="img" aria-label="Grey faceted background">
  <div class="line shadow" style="left:0;right:0;text-align:center;top:78px;font-size:21px">GET YOUR</div>
  <div class="line shadow" style="left:12px;top:144px;font-size:32px;color:var(--pink)">FREE</div>
  <div class="line shadow" style="right:12px;top:182px;font-size:30px;color:var(--pink)">GUIDE</div>
  <div class="line shadow" style="left:0;right:0;text-align:center;top:264px;font-size:23px">SUCCESSFUL</div>
  <div class="line shadow" style="left:0;right:0;text-align:center;top:291px;font-size:17px">CROWDFUNDING</div>
  <div class="cta tall" style="left:9px;top:393px;width:143px;height:38px"><span>LEARN MORE</span>
    <svg viewBox="0 0 18 18"><circle cx="9" cy="9" r="8" fill="#fff"/><path d="M7 5l5 4-5 4z" fill="#4cb51c"/></svg></div>
  <div class="foot-strip"></div>
</div>

<!-- skyscraper: deep blue -->
<div class="brand-dot" style="left:445px;top:297px;width:66px;height:66px"></div>
<div class="line brand-name vertical" style="left:397px;width:160px;text-align:center;top:364px;font-size:22px">Fundlark</div>
<div class="line brand-tag" style="left:397px;width:160px;text-align:center;top:391px;font-size:13px;line-height:14.5px;white-space:normal">Project + Crowd<br>=<br>Funding</div>
<div class="banner bg-deep zig-top" style="left:397px;top:445px;width:160px;height:445px" role="img" aria-label="Deep blue faceted background">
  <div class="line shadow" style="left:0;right:0;text-align:center;top:78px;font-size:21px">GET YOUR</div>
  <div class="line shadow" style="left:12px;top:144px;font-size:32px;color:var(--green-text)">FREE</div>
  <div class="line shadow" style="right:12px;top:182px;font-size:30px;color:var(--green-text)">GUIDE</div>
  <div class="line shadow" style="left:0;right:0;text-align:center;top:264px;font-size:23px">SUCCESSFUL</div>
  <div class="line shadow" style="left:0;right:0;text-align:center;top:291px;font-size:17px">CROWDFUNDING</div>
  <div class="cta tall" style="left:9px;top:393px;width:143px;height:38px"><span>LEARN MORE</span>
    <svg viewBox="0 0 18 18"><circle cx="9" cy="9" r="8" fill="#fff"/><path d="M7 5l5 4-5 4z" fill="#4cb51c"/></svg></div>
  <div class="foot-strip"></div>
</div>

<!-- small squares -->
<div class="banner bg-charcoal" style="left:605px;top:676px;width:180px;height:160px" role="img" aria-label="Grey faceted background">
  <div class="line" style="left:5px;top:8px;font-size:15px;color:var(--pink);line-height:20px">GET YOUR<br>FREE GUIDE TO</div>
  <div class="line shadow" style="left:11px;top:62px;font-size:19px;line-height:24px">SUCCESSFUL<br>CROWDFUNDING</div>
  <div class="cta" style="left:23px;top:124px;width:117px;height:31px"><span>Learn More</span>
    <svg viewBox="0 0 18 18"><circle cx="9" cy="9" r="8" fill="#fff"/><path d="M7 5l5 4-5 4z" fill="#4cb51c"/></svg></div>
</div>
<div class="banner bg-deep" style="left:805px;top:676px;width:180px;height:160px" role="img" aria-label="Deep blue faceted background">
  <div class="line" style="left:5px;top:8px;font-size:15px;color:var(--pink);line-height:20px">GET YOUR<br>FREE GUIDE TO</div>
  <div class="line shadow" style="left:11px;top:62px;font-size:19px;line-height:24px">SUCCESSFUL<br>CROWDFUNDING</div>
  <div class="cta" style="left:23px;top:124px;width:117px;height:31px"><span>Learn More</span>
    <svg viewBox="0 0 18 18"><circle cx="9" cy="9" r="8" fill="#fff"/><path d="M7 5l5 4-5 4z" fill="#4cb51c"/></svg></div>
</div>
<div class="banner bg-plum" style="left:997px;top:676px;width:180px;height:160px" role="img" aria-label="Purple faceted background">
  <div class="line" style="left:5px;top:8px;font-size:15px;color:var(--green-text);line-height:20px">GET YOUR<br>FREE GUIDE TO</div>
  <div class="line shadow" style="left:11px;top:62px;font-size:19px;line-height:24px">SUCCESSFUL<br>CROWDFUNDING</div>
  <div class="cta" style="left:23px;top:124px;width:117px;height:31px"><span>Learn More</span>
    <svg viewBox="0 0 18 18"><circle cx="9" cy="9" r="8" fill="#fff"/><path d="M7 5l5 4-5 4z" fill="#4cb51c"/></svg></div>
</div>

</body>
</html>
```